Aquatic View

We need a web design for a new window cleaning company name Tidal Pane Care. We are located in Grand Cayman, Cayman Islands. We are a small company, a team of husband and wife. Our services include residencial interior and exterior window cleaning and commercial. Extra services such as ceiling fans cleaning, mirrors, high dusting. Home cleaning services. Power washing. Explaining the service. We want a modern, beachy style with aquatic colors. We want to use our domain name "tidalpanecare.ky". We want to portray a clean, modern and professional design.

Target Market(s)

Big Home owners

Industry/Entity Type

Cleaning Service

Contact Information for Business Card

Company Name: Tidal Pane Care
Name: Dennis Okafor owner/manager
Phone: 345-5550194
Email: dennis@tidalpanecare.ky
Website: tidalpanecare.ky
Address: P.O.Box 4820 GT, George Town, Grand Cayman KY1-2043 Cayman Islands

Number of Pages Required

2 page

Font styles to use
Sans Serif

Colors
0592cd
0455a3
33a6d7
85cae6
cadf82
abd036
fbf289

Requirements
Nice to have
• Pictures of an ocean view and palm trees from clear windows.
• https://quelvaro.com/bidmatic/
• Use the above for "free estimate".

```html
<!DOCTYPE html>
<html lang="en">
<head>
<meta charset="utf-8">
<title>Tidal Pane Care — Window Cleaning Service</title>
<link rel="stylesheet" href="https://fonts.googleapis.com/css2?family=Open+Sans:wght@300;400;600;700&display=swap">
<style>
:root{
  --ocean:#0592cd;
  --deep:#0455a3;
  --sky:#33a6d7;
  --foam:#85cae6;
  --lime-soft:#cadf82;
  --lime:#abd036;
  --sand:#fbf289;
  --ink:#3b4650;
  --muted:#6c7780;
  --olive:#7a9a12;
  --white:#ffffff;
}
*{box-sizing:border-box;margin:0;padding:0}
html,body{width:1200px;height:3308px;overflow:hidden}
body{font-family:'Open Sans',Arial,sans-serif;color:var(--ink);background:var(--white);position:relative}
.abs{position:absolute}

.topbar{left:0;top:0;width:1200px;height:44px;background:var(--ocean);color:var(--white);font-size:13px}
.topbar span{position:absolute;top:13px;display:flex;align-items:center;gap:7px}
.topbar svg{width:13px;height:13px}

.header{left:0;top:44px;width:1200px;height:80px;background:var(--white)}
.brand{position:absolute;left:180px;top:18px;display:flex;align-items:center;gap:10px}
.brand-mark{width:36px;height:36px;border-radius:50%;background:var(--ocean)}
.brand-name{font-size:26px;font-weight:700;color:var(--deep);letter-spacing:.5px}
.call{position:absolute;left:668px;top:20px;display:flex;gap:10px;align-items:center}
.call svg{width:20px;height:34px}
.call small{display:block;font-size:10px;color:var(--muted);letter-spacing:.3px}
.call strong{display:block;font-size:17px;font-weight:400;color:var(--ocean)}
.divider{position:absolute;left:850px;top:18px;width:1px;height:44px;background:#cfd6db}
.socials{position:absolute;left:868px;top:22px;display:flex;gap:7px}
.socials i{width:32px;height:32px;border-radius:50%;background:var(--lime);display:block}

.nav{left:0;top:124px;width:1200px;height:42px;background:var(--ocean)}
.nav ul{list-style:none;display:flex;position:absolute;left:218px;top:13px;gap:40px}
.nav li{color:var(--white);font-size:12px;font-weight:600;text-transform:uppercase}
.quote{left:860px;top:114px;width:156px;height:40px;background:var(--lime);color:var(--deep);font-weight:700;font-size:17px;display:flex;align-items:center;justify-content:center;border-radius:0 0 6px 6px}

.hero{left:0;top:166px;width:1200px;height:502px;background:linear-gradient(180deg,#cfe4ef 0%,#6fa8c9 35%,#2c8ab3 55%,#e8eef0 75%,#d8dfe2 100%)}
.cta{left:0;top:668px;width:1200px;height:79px;background:var(--ocean)}
.cta h2{position:absolute;left:188px;top:20px;font-size:28px;font-weight:300;color:var(--white);letter-spacing:.5px}
.cta h2 b{font-weight:700}
.cta .btn{position:absolute;left:804px;top:18px;width:186px;height:44px;background:var(--lime);color:var(--white);font-size:21px;display:flex;align-items:center;justify-content:center}

.services{left:0;top:747px;width:1200px;height:893px;background:linear-gradient(160deg,#f2f3f4 0%,#e6e9eb 55%,#dfe3e6 100%)}
.services-art{left:70px;top:1230px;width:330px;height:410px;background:linear-gradient(135deg,rgba(200,215,224,.6),rgba(170,195,210,.3));border-radius:10px}
.sec-title{position:absolute;width:1200px;text-align:center;font-size:19px;color:var(--deep);font-weight:600}
.rule{position:absolute;left:556px;width:90px;height:12px}
.timeline{left:600px;top:880px;width:2px;height:680px;background:var(--ocean)}
.svc-icon{position:absolute;width:66px;height:66px;border-radius:50%;background:var(--white);border:3px solid var(--ocean);display:flex;align-items:center;justify-content:center}
.svc-icon svg{width:34px;height:34px}
.svc{position:absolute;width:260px}
.svc h3{font-size:17px;font-weight:400;color:var(--olive);line-height:1.2}
.svc p{font-size:11px;color:var(--muted);margin-top:8px;line-height:1.4}
.svc.left{left:289px;text-align:right}
.svc.right{left:651px}

.about{left:0;top:1640px;width:1200px;height:458px;background:var(--lime)}
.about-panel{left:445px;top:1700px;width:755px;height:336px;background:var(--white)}
.about-photo{left:0;top:1700px;width:445px;height:336px;background:linear-gradient(135deg,#9fb7c4,#2e6aa6 55%,#6b8f5e)}
.about-text{left:465px;top:1700px;width:560px}
.about-text h2{font-size:18px;font-weight:400;color:var(--ink)}
.about-text .rule2{width:90px;height:12px;margin:4px 0 10px 0}
.about-text p{font-size:10.5px;line-height:1.55;color:var(--muted)}
.more{display:inline-block;margin-top:10px;border:1px solid var(--ink);font-size:10px;padding:3px 12px;color:var(--ink)}
.feature{display:flex;align-items:center;gap:10px;margin-top:18px}
.feature i{width:36px;height:36px;background:var(--deep);border-radius:4px;display:flex;align-items:center;justify-content:center}
.feature h3{font-size:16px;font-weight:600;color:var(--ink)}

.booking-photo{left:0;top:2098px;width:599px;height:458px;background:linear-gradient(120deg,#eef1f3,#c6d0d6 50%,#5d6f8f)}
.booking{left:599px;top:2098px;width:601px;height:458px;background:var(--sky)}
.booking h2{position:absolute;left:42px;top:26px;font-size:20px;font-weight:600;color:var(--white)}
.field{position:absolute;height:27px;background:#d8eef8;border:1px solid #b9dff0;font-size:10px;color:#50606b;padding:7px 8px;display:flex;justify-content:space-between;align-items:center}
.field svg{width:9px;height:9px}
.submit{position:absolute;left:346px;top:416px;width:72px;height:22px;background:var(--deep);color:var(--white);font-size:10px;display:flex;align-items:center;justify-content:center;letter-spacing:.5px}

.testimonials{left:0;top:2556px;width:1200px;height:492px;background:linear-gradient(180deg,#3d82ad 0%,#7ab3cf 45%,#c9dbe3 100%)}
.testimonials .sec-title{top:38px;color:var(--ink);font-weight:400;font-size:21px}
.card{position:absolute;top:141px;width:186px;height:304px;background:var(--foam)}
.card .top{height:104px;display:flex;align-items:center;justify-content:center}
.card .avatar{width:86px;height:86px;border-radius:50%;background:rgba(255,255,255,.55)}
.card p{font-size:10.5px;line-height:1.45;color:var(--ink);padding:50px 12px 0 12px}
.card .name{position:absolute;left:0;bottom:0;width:186px;height:26px;background:var(--white);font-size:11px;font-weight:600;text-align:center;line-height:26px;text-transform:uppercase}
.arrow{position:absolute;top:274px;width:26px;height:26px;background:var(--white);display:flex;align-items:center;justify-content:center}
.arrow svg{width:10px;height:10px}

.footer{left:0;top:3048px;width:1200px;height:198px;background:var(--lime-soft)}
.footer-wave{left:0;top:3030px;width:1200px;height:40px}
.fcol{position:absolute;top:74px;display:flex;gap:14px}
.fcol svg{width:16px;height:16px;margin-top:2px}
.fcol h4{font-size:13px;color:var(--deep);font-weight:600;margin-bottom:6px}
.fcol p{font-size:11px;line-height:1.5;color:var(--ink)}
.bottombar{left:0;top:3246px;width:1200px;height:62px;background:var(--deep)}
.bottombar .mini{position:absolute;left:541px;top:9px;display:flex;gap:10px}
.bottombar .mini i{width:14px;height:14px;border-radius:50%;background:var(--white);display:block}
.bottombar .copy{position:absolute;left:0;width:1200px;top:34px;text-align:center;color:var(--white);font-size:11px}
.pay{position:absolute;left:905px;top:22px;display:flex;gap:6px}
.pay i{width:30px;height:18px;border-radius:3px;background:var(--foam);display:block}
</style>
</head>
<body>

<div class="abs topbar">
  <span style="left:180px">WINDOW CLEANING SERVICE</span>
  <span style="left:556px"><svg viewBox="0 0 16 12"><rect x="0.5" y="0.5" width="15" height="11" fill="none" stroke="#fff"/><path d="M1 1l7 6 7-6" fill="none" stroke="#fff"/></svg>info@tidalpanecare.ky</span>
  <span style="left:755px"><svg viewBox="0 0 16 16"><circle cx="8" cy="8" r="7" fill="none" stroke="#fff" stroke-width="1.5"/><path d="M8 4v4l3 2" fill="none" stroke="#fff" stroke-width="1.5"/></svg>WORKING HOURS : MON-SAT (8:00AM - 5:00PM)</span>
</div>

<header class="abs header">
  <div class="brand"><i class="brand-mark"></i><span class="brand-name">Tidal Pane Care</span></div>
  <div class="call">
    <svg viewBox="0 0 20 34"><rect x="2" y="1" width="16" height="32" rx="3" fill="none" stroke="#0592cd" stroke-width="2"/><circle cx="10" cy="28" r="1.8" fill="#0592cd"/></svg>
    <div><small>CALL US FOR FREE CONSULTING</small><strong>345-5550194</strong></div>
  </div>
  <i class="divider"></i>
  <div class="socials"><i></i><i></i><i></i><i></i></div>
</header>

<nav class="abs nav">
  <ul><li>Home</li><li>About Us</li><li>Services</li><li>Career</li><li>Contact</li></ul>
</nav>
<div class="abs quote">GET A QUOTE</div>

<div class="abs hero" role="img" aria-label="Bright dining room with glass walls looking out over an infinity pool, palm trees and the sea"></div>

<section class="abs cta">
  <h2>GET A CLEAR <b>VIEW</b> THROUGH YOUR WINDOW</h2>
  <div class="btn">BOOK NOW</div>
</section>

<section class="abs services"></section>
<div class="abs services-art" role="img" aria-label="Hand holding a squeegee on a wet window"></div>
<h2 class="sec-title" style="top:778px">Our Services</h2>
<svg class="rule" style="top:812px" viewBox="0 0 90 12"><line x1="0" y1="6" x2="90" y2="6" stroke="#8a969e" stroke-width="1.5"/><rect x="82" y="0" width="6" height="12" fill="#8a969e"/></svg>
<div class="abs timeline"></div>

<div class="svc-icon" style="left:568px;top:875px"><svg viewBox="0 0 34 34" fill="none" stroke="#0592cd" stroke-width="2"><path d="M4 17L17 6l13 11"/><path d="M8 15v13h18V15"/><rect x="14" y="20" width="6" height="8"/></svg></div>
<div class="svc left" style="top:872px"><h3>Residential Window Cleaning<br>(Interior and Exterior)</h3><p>Clear glass inside and out,<br>done with care every visit.</p></div>

<div class="svc-icon" style="left:568px;top:1006px"><svg viewBox="0 0 34 34" fill="none" stroke="#0592cd" stroke-width="2"><rect x="6" y="4" width="22" height="26"/><path d="M11 9h4M19 9h4M11 15h4M19 15h4M11 21h4M19 21h4"/></svg></div>
<div class="svc right" style="top:1000px"><h3>Commercial Window Cleaning<br>(Interior and Exterior)</h3><p>Spotless fronts and offices,<br>on a schedule that suits you.</p></div>

<div class="svc-icon" style="left:568px;top:1132px"><svg viewBox="0 0 34 34" fill="none" stroke="#0592cd" stroke-width="2"><path d="M17 4v10"/><circle cx="17" cy="17" r="3"/><path d="M14 17H3M20 17h11M17 20l-5 10M17 20l5 10"/></svg></div>
<div class="svc left" style="top:1126px"><h3>Ceiling Fans<br>Cleaning</h3><p>Dust-free blades and housings,<br>for fresher air at home.</p></div>

<div class="svc-icon" style="left:568px;top:1258px"><svg viewBox="0 0 34 34" fill="none" stroke="#0592cd" stroke-width="2"><circle cx="17" cy="17" r="12"/><path d="M11 19l8-8M14 23l9-9"/></svg></div>
<div class="svc right" style="top:1254px"><h3>Mirrors<br>Cleaning</h3><p>Streak-free mirrors in every<br>room, bath and hallway.</p></div>

<div class="svc-icon" style="left:568px;top:1387px"><svg viewBox="0 0 34 34" fill="none" stroke="#0592cd" stroke-width="2"><path d="M26 4L12 20"/><path d="M12 20l-6 8 10-4z"/></svg></div>
<div class="svc left" style="top:1380px"><h3>High Dusting<br>Cleaning</h3><p>Beams, vents and high ledges,<br>reached safely and cleaned.</p></div>

<div class="svc-icon" style="left:568px;top:1516px"><svg viewBox="0 0 34 34" fill="none" stroke="#0592cd" stroke-width="2"><path d="M6 28l12-12"/><rect x="17" y="9" width="8" height="8" transform="rotate(45 21 13)"/><path d="M25 5l4-1M27 9l4 0M23 3l1-2"/></svg></div>
<div class="svc right" style="top:1514px"><h3>Power washing</h3><p>Driveways, decks and walls,<br>washed back to bright.</p></div>

<section class="abs about"></section>
<div class="abs about-panel"></div>
<div class="abs about-photo" role="img" aria-label="Window cleaner in blue uniform washing a large glass pane"></div>
<div class="abs about-text">
  <h2>ABOUT US</h2>
  <svg class="rule2" viewBox="0 0 90 12"><line x1="0" y1="6" x2="90" y2="6" stroke="#8a969e" stroke-width="1.5"/><rect x="82" y="0" width="6" height="12" fill="#8a969e"/></svg>
  <p>We are a small husband and wife team based in Grand Cayman, and we treat every home as if it were our own. From wide ocean-view windows to the smallest mirror, we bring the right tools, a careful eye and a friendly smile. Our goal is simple: glass so clear you forget it is there, so you can enjoy the island light and the view you paid for. We work around your day, protect your floors and furniture, and leave nothing behind but a fresh, bright home.</p>
  <div class="more">VIEW MORE</div>
  <div class="feature"><i><svg width="20" height="20" viewBox="0 0 20 20" fill="none" stroke="#fff" stroke-width="2"><circle cx="9" cy="11" r="6"/><path d="M12 8l6-6"/></svg></i><h3>Fast &amp; Effective Service (Modern tools)</h3></div>
  <p style="margin-top:10px">We use pure water poles, soft brushes and eco friendly cleaners that are safe for your family, pets and garden. Modern gear lets us reach high windows quickly and safely, so the job is done well, on time and without streaks or fuss.</p>
</div>

<div class="abs booking-photo" role="img" aria-label="Hand wiping a window with a dark blue microfibre cloth and spray bottle"></div>
<section class="abs booking">
  <h2>Service Booking form</h2>
  <div class="field" style="left:42px;top:77px;width:183px">Name</div>
  <div class="field" style="left:237px;top:77px;width:181px">Email id</div>
  <div class="field" style="left:42px;top:116px;width:376px">Address</div>
  <div class="field" style="left:42px;top:154px;width:183px">Phone No</div>
  <div class="field" style="left:237px;top:154px;width:181px">No of Floors<svg viewBox="0 0 10 10"><path d="M1 3l4 4 4-4z" fill="#50606b"/></svg></div>
  <div class="field" style="left:42px;top:193px;width:183px">Project Type<svg viewBox="0 0 10 10"><path d="M1 3l4 4 4-4z" fill="#50606b"/></svg></div>
  <div class="field" style="left:237px;top:193px;width:181px">Area (SqFt)<svg viewBox="0 0 10 10"><path d="M1 3l4 4 4-4z" fill="#50606b"/></svg></div>
  <div class="field" style="left:42px;top:231px;width:183px">Basement<svg viewBox="0 0 10 10"><path d="M1 3l4 4 4-4z" fill="#50606b"/></svg></div>
  <div class="field" style="left:237px;top:231px;width:181px">Service Date<svg viewBox="0 0 10 10"><rect x="1" y="2" width="8" height="7" fill="none" stroke="#50606b"/><line x1="1" y1="4" x2="9" y2="4" stroke="#50606b"/></svg></div>
  <div class="field" style="left:42px;top:270px;width:376px;height:133px;align-items:flex-start">Message</div>
  <div class="submit">SUBMIT</div>
</section>

<section class="abs testimonials">
  <h2 class="sec-title">TESTIMONIALS</h2>
  <svg class="rule" style="top:76px" viewBox="0 0 90 12"><line x1="0" y1="6" x2="90" y2="6" stroke="#3b4650" stroke-width="1.5"/><rect x="82" y="0" width="6" height="12" fill="#3b4650"/></svg>
  <div class="arrow" style="left:135px"><svg viewBox="0 0 10 10"><path d="M7 1L2 5l5 4z" fill="#3b4650"/></svg></div>
  <div class="arrow" style="left:1038px"><svg viewBox="0 0 10 10"><path d="M3 1l5 4-5 4z" fill="#3b4650"/></svg></div>

  <div class="card" style="left:178px"><div class="top" style="background:var(--sand)"><i class="avatar" role="img" aria-label="Customer portrait"></i></div><p>Our sea view windows have never looked so clear. Friendly, careful and right on time every single visit we book.</p><div class="name">Mara Quill</div></div>
  <div class="card" style="left:398px"><div class="top" style="background:var(--foam)"><i class="avatar" role="img" aria-label="Customer portrait"></i></div><p>They cleaned every pane of our office front in one morning. No streaks, no mess, and fair prices too for us.</p><div class="name">Theo Brandt</div></div>
  <div class="card" style="left:616px"><div class="top" style="background:#f6d48a"><i class="avatar" role="img" aria-label="Customer portrait"></i></div><p>The ceiling fans and high shelves were spotless after their visit. We will have them back again every season.</p><div class="name">Ivo Castell</div></div>
  <div class="card" style="left:836px"><div class="top" style="background:var(--lime-soft)"><i class="avatar" role="img" aria-label="Customer portrait"></i></div><p>Our driveway and deck look brand new after the power wash. Kind team, quick work and great value for money.</p><div class="name">Lena Moss</div></div>
</section>

<svg class="abs footer-wave" viewBox="0 0 1200 40" preserveAspectRatio="none"><path d="M0 18 Q600 -10 1200 18 V40 H0z" fill="#cadf82"/></svg>
<footer class="abs footer">
  <div class="fcol" style="left:173px"><svg viewBox="0 0 16 16"><path d="M8 1a5 5 0 0 1 5 5c0 4-5 9-5 9S3 10 3 6a5 5 0 0 1 5-5z" fill="#0455a3"/><circle cx="8" cy="6" r="2" fill="#cadf82"/></svg><div><h4>Address</h4><p>P.O.Box 4820 GT, George Town<br>Grand Cayman KY1-2043<br>Cayman Islands</p></div></div>
  <div class="fcol" style="left:408px"><svg viewBox="0 0 16 16"><path d="M3 1l3 0 1 4-2 1c1 2 3 4 5 5l1-2 4 1v3c0 1-1 2-2 2C7 15 1 9 1 3c0-1 1-2 2-2z" fill="#0455a3"/></svg><div><h4>Phone</h4><p>345-5550194<br>Dennis Okafor</p></div></div>
  <div class="fcol" style="left:606px"><svg viewBox="0 0 16 12"><rect x="0" y="0" width="16" height="12" fill="#0455a3"/><path d="M1 1l7 6 7-6" fill="none" stroke="#cadf82"/></svg><div><h4>Email</h4><p>info@tidalpanecare.ky<br>dennis@tidalpanecare.ky</p></div></div>
  <div class="fcol" style="left:836px"><svg viewBox="0 0 16 16"><circle cx="8" cy="8" r="7" fill="#0455a3"/><path d="M8 4v4l3 2" fill="none" stroke="#cadf82" stroke-width="1.5"/></svg><div><h4>Opening Hours</h4><p>Mon-Sat : 8AM to 5PM<br>We close only Sunday</p></div></div>
</footer>

<div class="abs bottombar">
  <div class="mini"><i></i><i></i><i></i><i></i></div>
  <div class="copy">© 2015 Tidal Pane Care, All Rights Reserved</div>
  <div class="pay"><i></i><i></i><i></i><i></i></div>
</div>

</body>
</html>
```